Book Cover Design (poetry, prose, and original quotes Book) - Title: resonance & reflection

FIRSTLY - my name is MARGOT VELDHUIS (pls use this)

Looking for a soft cover design (6" X 9") as well as an e-book cover design. I have ISBN bar code already. This soft cover will need spine design and area for back cover blurb. Number of pages is approx 210. The page count might change, but only by a few pages if anything.
The book is a collection of poems, prose, and quotes with chapter titles such as: pain, growth, hope, trust, love, and...so it is. It's meant to be inspiring and also a go to book people will reach for when searching for truth.

Tavi Mendel and Odo Marrek are similar in nature to content.

I have attached an PIXORAMA image that I am thinking of.
Lower case in title and in my name (author)
San Serif font.

I like the idea of the book title to be along the lateral line (where water meets the sky).

I am open to book cover ideas like the poets noted above, but that style seems to be saturating the genre.

Target Market(s)

Will be selling on QBL (Borvex). Audience are people who are on a journey of self-discovery, personal empowerment, and spirituality.

Industry/Entity Type

Spiritual / Personal Growth / Poetry

Font styles to use
Sans Serif
Other font styles liked:
• Simplifica, alcubierre, stellar, gantic, kiona

Requirements
Must have
• Front, Spine, and Back cover / lower case in title and author's name
Nice to have
• I do like the look of Tavi Mendel and Odo Marrek's books, but I feel that style might be over done now, but I am open to a modern simple style like their books (see examples below). I would like my book to convey the feeling of resonance (vibration) and reflection (thoughts, ideas as a result of meditation)
Should not have
• I prefer simple designs, not a lot of clutter, or heavy typefaces. Definately do not want anything like birds or butterflies.

```html
<!DOCTYPE html>
<html lang="en">
<head>
<meta charset="utf-8">
<title>resonance &amp; reflection — margot veldhuis</title>
<link rel="stylesheet" href="https://fonts.googleapis.com/css2?family=Questrial&family=Montserrat:wght@400&display=swap">
<style>
  :root {
    --backdrop-centre: #f2f3f3;
    --backdrop-edge: #d9dbdb;
    --sky-high: #d6e1ea;
    --sky-low: #c4d4e2;
    --ridge: #6a7d90;
    --shore: #1c232b;
    --water-dark: #2a3540;
    --water-mid: #7f93a8;
    --water-light: #b9c6d4;
    --water-deep: #6c7f94;
    --type: #ffffff;
  }
  * { margin: 0; padding: 0; box-sizing: border-box; }
  html, body { width: 1200px; height: 1200px; overflow: hidden; }
  body {
    background: radial-gradient(circle at 50% 50%, var(--backdrop-centre) 0%, var(--backdrop-edge) 100%);
    position: relative;
  }
  .book-cover {
    position: absolute;
    left: 279px;
    top: 118px;
    width: 643px;
    height: 964px;
    overflow: hidden;
  }
  .cover-photo {
    position: absolute;
    inset: 0;
    background: linear-gradient(to bottom,
      var(--sky-high) 0%,
      var(--sky-low) 42%,
      var(--ridge) 50%,
      var(--shore) 60%,
      var(--shore) 63%,
      var(--water-dark) 70%,
      var(--water-mid) 82%,
      var(--water-light) 90%,
      var(--water-deep) 100%);
  }
  .title {
    position: absolute;
    left: 0;
    right: 0;
    text-align: center;
    font-family: "Questrial", sans-serif;
    font-size: 37px;
    letter-spacing: 3.4px;
    color: var(--type);
    line-height: 1;
    white-space: nowrap;
  }
  .title--main { top: 572px; }
  .title--mirror {
    top: 606px;
    transform: scaleY(-1);
    opacity: 0.28;
    filter: blur(0.6px);
  }
  .author {
    position: absolute;
    left: 0;
    right: 0;
    top: 855px;
    text-align: center;
    font-family: "Montserrat", sans-serif;
    font-weight: 400;
    font-size: 23px;
    letter-spacing: 0.3px;
    color: var(--type);
  }
</style>
</head>
<body>
  <main class="book-cover">
    <div class="cover-photo" role="img" aria-label="Photograph of a still mountain lake at dawn, forested slopes meeting the water with their mirror image below"></div>
    <h1 class="title title--main">resonance &amp; reflection</h1>
    <div class="title title--mirror" aria-hidden="true">resonance &amp; reflection</div>
    <p class="author">margot veldhuis</p>
  </main>
</body>
</html>
```